Redesign of WordHarbor.com in Bootstrap 4

Current design of WordHarbor.com is not responsive. We need to change it to latest version of Bootstrap 4 keeping essential elements in place.

Apart from home page, we need designs for http://www.wordharbor.com/meaning/cat also.

Coding

Coded - Design and coding required

Number of Pages Required

2 page

Colors
34a7d8

Requirements
Must have
• Bootstrap 4

```html
<!DOCTYPE html>
<html lang="en">
<head>
<meta charset="utf-8">
<title>WordHarbor – Home</title>
<link href="https://fonts.googleapis.com/css2?family=Open+Sans:wght@400;600&family=Raleway:wght@400;500;600&family=Poiret+One&display=swap" rel="stylesheet">
<style>
:root{
  --brand:#34a7d8;
  --brand-dark:#0f6cc0;
  --ink:#1c1c1c;
  --bar:#222222;
  --btn:#2b2b2b;
  --white:#ffffff;
  --muted:#8a8a8a;
  --tidbit:#e2efcd;
  --panel:#ececec;
  --accent:#e39a1f;
}
*{box-sizing:border-box;margin:0;padding:0}
html,body{width:820px;height:1200px;overflow:hidden}
body{font-family:"Open Sans",Arial,sans-serif;background:var(--brand);color:var(--ink);position:relative}
.abs{position:absolute}

.topbar{left:0;top:0;width:820px;height:30px;background:var(--ink)}
.social{left:88px;top:10px;display:flex;gap:13px}
.social span{width:10px;height:10px;border-radius:50%;background:#ddd;display:block}
.login{right:88px;top:7px;display:flex;align-items:center;font-size:7px;color:#fff}
.login label{margin-right:6px}
.login .field{width:100px;height:12px;border-bottom:1px solid #888;margin-right:12px;font-size:6px;color:#777;line-height:10px;padding-left:2px}
.login .btn{background:var(--brand);color:#fff;font-size:7px;padding:4px 10px;margin-left:0}

.header{left:0;top:30px;width:820px;height:107px;background:var(--brand)}
.logo{left:90px;top:48px;display:flex;align-items:center;gap:5px;font-family:"Raleway",sans-serif;font-weight:600;font-size:19px;color:var(--ink)}
.logo i{width:10px;height:10px;border-radius:50%;background:var(--accent);display:block}
.join{left:626px;top:52px;width:104px;height:21px;background:#2d2d2d;color:#fff;font-size:10px;line-height:21px;text-align:right;padding-right:10px;border-radius:2px}
.nav{left:92px;top:100px;display:flex;gap:25px}
.nav a{width:86px;height:25px;background:var(--btn);color:#fff;font-size:8.5px;line-height:25px;text-align:center;text-decoration:none;box-shadow:0 1px 2px rgba(0,0,0,.4);font-family:"Raleway",sans-serif;font-weight:500}
.nav a.active{background:var(--brand-dark)}

.hero{left:0;top:137px;width:820px;height:328px;background:radial-gradient(ellipse at 50% 60%,#4a3a33 0%,#2a211d 45%,#0c0a09 100%)}
.hero h1{left:0;top:70px;width:820px;text-align:center;font-family:"Poiret One",sans-serif;font-weight:400;font-size:28px;color:#fff}
.search{left:131px;top:125px;width:559px;height:46px;background:var(--brand-dark);padding:4px}
.search .box{display:flex;width:100%;height:100%;border:1px solid #fff;background:#fff}
.search .input{flex:1;font-size:10px;color:#999;line-height:34px;padding-left:12px}
.search .input em{color:#aaa}
.search .go{width:77px;background:#151515;color:var(--accent);font-size:10px;line-height:34px;text-align:center}
.features{font-size:10px;color:#eee;line-height:14px}
.features li{list-style:none;position:relative;padding-left:15px;margin-bottom:11px}
.features li::before{content:"";position:absolute;left:0;top:3px;width:8px;height:8px;border-radius:50%;background:var(--brand)}
.dots{left:390px;top:312px;display:flex;gap:3px}
.dots span{width:6px;height:6px;border-radius:50%;background:#aaa}
.dots span:first-child{background:var(--brand)}

.browse{left:0;top:465px;width:820px;height:43px;background:var(--bar);display:flex;align-items:center;padding-left:90px;font-size:9px;color:#fff;font-family:"Raleway",sans-serif}
.browse .label{margin-right:12px}
.browse .letters{display:flex;gap:3px}
.browse .letters span{width:18px;height:18px;border:1px solid #ccc;font-size:8.5px;text-align:center;line-height:16px}
.browse .letters span.on{background:var(--brand);border-color:var(--brand)}

.crossword{left:90px;top:522px;width:452px;height:206px;background:linear-gradient(135deg,#6f6f6f,#a5a5a5 50%,#4e4e4e);text-align:center}
.crossword h2{margin-top:62px;font-family:"Raleway",sans-serif;font-weight:500;font-size:15px;color:var(--brand)}
.crossword p{font-size:8.5px;color:#111;margin-top:9px}
.dark-btn{display:inline-block;background:#111;color:#fff;font-size:9.5px;font-family:"Raleway",sans-serif;padding:8px 22px}
.crossword .dark-btn{margin-top:10px;width:106px;padding:8px 0}

.tidbit{left:557px;top:522px;width:171px;height:206px;background:var(--tidbit)}
.tidbit h3{position:absolute;left:19px;top:15px;font-family:"Raleway",sans-serif;font-weight:500;font-size:15px}
.tidbit .term{position:absolute;left:19px;top:44px;font-family:"Raleway",sans-serif;font-size:12px;color:var(--brand-dark)}
.tidbit p{position:absolute;left:19px;top:72px;width:134px;font-size:8.5px;line-height:16px;color:#777;text-align:justify}
.tidbit .arrows{position:absolute;left:133px;top:158px;font-size:10px;font-weight:600}
.tidbit .foot{position:absolute;left:0;bottom:0;width:171px;height:24px;background:#e6e6e6;display:flex;justify-content:space-between;align-items:center;padding:0 10px;font-size:7px;color:#666}

.addon{left:90px;top:742px;width:639px;height:165px;background:var(--panel);text-align:center}
.addon h2{margin-top:25px;font-family:"Raleway",sans-serif;font-weight:500;font-size:15px}
.addon h4{margin-top:8px;font-family:"Raleway",sans-serif;font-weight:600;font-size:12px}
.addon p{margin:9px auto 0;width:290px;font-size:9px;line-height:15px}
.addon .dark-btn{margin-top:10px;width:106px;padding:8px 0}
.press{left:630px;top:787px;width:72px;height:72px;border-radius:50%;background:#f7f7f7;box-shadow:0 4px 12px rgba(0,0,0,.25);text-align:center;font-size:8px}
.press .t{margin-top:14px;letter-spacing:.5px;border-bottom:1px solid #ccc;padding-bottom:4px;margin-left:10px;margin-right:10px;font-family:"Raleway",sans-serif}
.press .k{margin-top:6px;font-weight:600;font-size:7px}
.string{left:666px;top:742px;width:1px;height:45px;background:#333}

.mobile{left:92px;top:925px;width:636px;height:201px;background:linear-gradient(90deg,#2a1c1a,#5a2d2b 35%,#3b2523 60%,#120c0b)}
.mobile .copy{position:absolute;left:26px;top:55px;width:228px;text-align:center;color:#fff}
.mobile h2{font-family:"Raleway",sans-serif;font-weight:500;font-size:15px}
.mobile p{font-size:9px;line-height:17px;margin-top:9px}
.store{display:inline-block;margin-top:10px;background:#111;border:1px solid #999;border-radius:4px;width:84px;height:29px;font-size:10px;line-height:27px;font-weight:600}
.device{position:absolute;left:390px;top:8px;width:210px;height:193px;background:linear-gradient(180deg,rgba(200,160,140,.25),rgba(180,130,110,.35))}
.device .screen{position:absolute;left:36px;top:6px;width:72px;height:158px;border-radius:10px;background:#111;padding:22px 5px}
.device .screen div{width:100%;height:106px;background:var(--brand)}

.footer{left:0;top:1141px;width:820px;height:59px;background:#111;color:#fff;text-align:center}
.footer nav{margin-top:18px;font-size:7.5px}
.footer nav a{color:#fff;text-decoration:none;margin:0 4px}
.footer .copy{font-size:7.5px;margin-top:9px}
</style>
</head>
<body>

<div class="abs topbar">
  <div class="abs social"><span></span><span></span><span></span><span></span><span></span></div>
  <div class="abs login">
    <label>User name :</label><div class="field">Enter user name</div>
    <label>Password :</label><div class="field"></div>
    <div class="btn">LOG IN</div>
  </div>
</div>

<header class="abs header"></header>
<div class="abs logo"><i></i>WordHarbor</div>
<div class="abs join">Join for FREE!</div>
<nav class="abs nav">
  <a class="active" href="#">HOME</a><a href="#">IDIOMS</a><a href="#">COMMON ERRORS</a><a href="#">CROSSWORD</a><a href="#">BLOG</a><a href="#">CONTACT</a>
</nav>

<section class="abs hero" role="img" aria-label="Dark photo of reading glasses resting in front of stacked books">
  <h1 class="abs">Search, Save and Master Words</h1>
  <div class="abs search"><div class="box"><div class="input">Enter a word or phrase &nbsp;<em>(eg. symbol, grace, explanation)</em></div><div class="go">SEARCH</div></div></div>
  <ul class="abs features" style="left:92px;top:214px"><li>Search from more than 300,000 words and phrases.</li><li>Audio, phonetics, meanings, synonyms and antonyms</li></ul>
  <ul class="abs features" style="left:415px;top:214px"><li>Multiple usages to clarify the context.</li><li>Save the words to your personal deck and access from anywhere</li></ul>
  <div class="abs dots"><span></span><span></span><span></span><span></span><span></span></div>
</section>

<div class="abs browse">
  <span class="label">Browse Dictionary :</span>
  <div class="letters"><span class="on">A</span><span>B</span><span>C</span><span>D</span><span>E</span><span>F</span><span>G</span><span>H</span><span>I</span><span>J</span><span>K</span><span>L</span><span>M</span><span>N</span><span>O</span><span>P</span><span>Q</span><span>R</span><span>S</span><span>T</span><span>U</span><span>V</span><span>W</span><span>X</span><span>Y</span><span>Z</span></div>
</div>

<section class="abs crossword" role="img" aria-label="Photo of a pencil resting on a crossword puzzle grid">
  <h2>DAILY CROSSWORD</h2>
  <p>Take this daily crossword challenge from WordHarbor.</p>
  <span class="dark-btn">SOLVE NOW</span>
</section>

<aside class="abs tidbit">
  <h3>ENGLISH TIDBIT</h3>
  <div class="term">gaffe/gaf</div>
  <p>"Gaffe" is a social blunder and "gaff" is a large hook. Be warned not to make the gaffe of mixing it up with gaff.</p>
  <div class="arrows"><span style="color:var(--brand-dark)">‹</span> ›</div>
  <div class="foot"><span>Gantlet / gauntlet</span><span>Theater / theatre</span></div>
</aside>

<section class="abs addon">
  <h2>EMBERFOX ADDON</h2>
  <h4>Quick Dictionary Lookup from WordHarbor.com</h4>
  <p>Add this tool to your Emberfox and quickly look up for definitions from any website without leaving the page.</p>
  <span class="dark-btn">GET IT NOW</span>
</section>
<div class="abs string"></div>
<div class="abs press"><div class="t">JUST PRESS</div><div class="k">SHIFT + 🖱</div></div>

<section class="abs mobile" role="img" aria-label="Blurred photo of books behind a hand holding a phone showing the app">
  <div class="copy">
    <h2>DESIGNED FOR POCKETPHONE</h2>
    <p>WordHarbor is specially designed for your Pocketphone to quickly lookup meaining, usages and audio of words.</p>
    <span class="store">App Market</span>
  </div>
  <div class="device"><div class="screen"><div></div></div></div>
</section>

<footer class="abs footer">
  <nav><a href="#">FAQ</a><a href="#">Contact</a><a href="#">BlogLegal</a><a href="#">Privacy Policy</a><a href="#">Terms of UseOthers</a><a href="#">Popular Words</a><a href="#">Common Errors in English</a><a href="#">Test Prep Online</a></nav>
  <div class="copy">Copyright © 2016 wordharbor.com. All rights reserved.</div>
</footer>

</body>
</html>
```